Esthetically Pleasing Core Values and Brand Promise for Accounting Firm

I would like a cohesive design that ties together my core values and brand promise. My firm, Maple Finch Advisory, provides accounting work to small businesses. I prefer modern and clean designs. I want my Core Values and Brand Promise to represent me - sole entrepreneur, married, mother of two kids, modern esthetics, clean lines, organized, colorful (teals, greys, white, yellows)

Industry/Entity Type

Public Accounting

Colors
33b8a4

```html
<!DOCTYPE html>
<html lang="en">
<head>
<meta charset="utf-8">
<title>Maple Finch Advisory — Core Values &amp; Brand Promise</title>
<link href="https://fonts.googleapis.com/css2?family=Barlow+Condensed:wght@600;700&family=Barlow:wght@300;500;700&display=swap" rel="stylesheet">
<style>
  :root {
    --backdrop: #00897a;
    --paper: #ffffff;
    --sky-teal: #4fabaf;
    --lime: #c1cc36;
    --deep-teal: #00877a;
    --mint: #33b8a4;
    --leaf: #7db343;
    --trunk: #e0e0e0;
    --ink: #142423;
    --shade: #1f3a36;
    --icon-line: #cfe9ea;
  }
  html, body { margin: 0; padding: 0; overflow: hidden; background: var(--backdrop); }
  .canvas { display: block; width: 725px; height: 1200px; }
  .headline { font-family: "Barlow Condensed", sans-serif; font-weight: 700; font-size: 162px; fill: var(--paper); }
  .value-title { font-family: "Barlow Condensed", sans-serif; font-weight: 700; font-size: 56px; fill: var(--paper); }
  .value-title-shadow { font-family: "Barlow Condensed", sans-serif; font-weight: 700; font-size: 56px; fill: var(--shade); }
  .value-copy { font-family: "Barlow", sans-serif; font-weight: 500; font-size: 17px; fill: var(--ink); letter-spacing: 0.4px; }
  .firm-name { font-family: "Barlow", sans-serif; font-weight: 300; fill: var(--deep-teal); letter-spacing: 4px; }
  .promise-title { font-family: "Barlow", sans-serif; font-weight: 700; font-size: 50px; fill: var(--deep-teal); letter-spacing: 1px; }
  .promise-label { font-family: "Barlow Condensed", sans-serif; font-weight: 700; font-size: 44px; fill: var(--paper); }
  .promise-icon { fill: none; stroke: var(--icon-line); stroke-width: 2.5; stroke-linecap: round; stroke-linejoin: round; }
</style>
</head>
<body>
<svg class="canvas" viewBox="0 0 1139 1884" xmlns="http://www.w3.org/2000/svg">
  <rect class="backdrop" width="1139" height="1884" fill="var(--backdrop)"/>

  <g class="poster">
    <rect class="poster-sheet" x="186" y="307" width="768" height="1271" fill="var(--paper)"/>
    <polygon class="header-band" points="186,307 604,307 692,725 300,738 186,625" fill="var(--sky-teal)"/>

    <text class="headline" x="245" y="478" textLength="268" lengthAdjust="spacingAndGlyphs">CORE</text>
    <text class="headline" x="245" y="610" textLength="375" lengthAdjust="spacingAndGlyphs">VALUES</text>

    <g class="firm-name-block">
      <text class="firm-name" x="708" y="422" font-size="44">MAPLE</text>
      <text class="firm-name" x="708" y="472" font-size="44">FINCH</text>
      <text class="firm-name" x="710" y="522" font-size="28">ADVISORY</text>
    </g>

    <rect class="tree-area" role="img" aria-label="Grey tree illustration growing from the brand promise into the four values"
      x="470" y="780" width="200" height="550" fill="var(--trunk)"/>

    <g class="value-tiles">
      <polygon class="tile tile-relentless" points="359,665 495,665 605,775 605,925 495,1035 359,1035 249,925 249,775" fill="var(--lime)"/>
      <polygon class="tile tile-empower" points="690,985 770,985 870,1085 870,1182 770,1282 690,1282 590,1182 590,1085" fill="var(--leaf)"/>
      <polygon class="tile tile-client" points="667,686 790,686 890,786 890,910 790,1010 667,1010 567,910 567,786" fill="var(--deep-teal)"/>
      <polygon class="tile tile-rectitude" points="352,985 465,985 555,1075 555,1195 465,1285 352,1285 262,1195 262,1075" fill="var(--mint)"/>
    </g>

    <g class="value-text">
      <text class="value-title-shadow" x="316" y="791" textLength="239" lengthAdjust="spacingAndGlyphs">RELENTLESS</text>
      <text class="value-title" x="313" y="788" textLength="239" lengthAdjust="spacingAndGlyphs">RELENTLESS</text>
      <text class="value-copy">
        <tspan x="320" y="823">We believe that the</tspan>
        <tspan x="320" y="845">longer we try to do our</tspan>
        <tspan x="320" y="867">best, the better we</tspan>
        <tspan x="320" y="888">become.</tspan>
      </text>

      <text class="value-title-shadow" x="658" y="780" textLength="130" lengthAdjust="spacingAndGlyphs">CLIENT</text>
      <text class="value-title" x="655" y="777" textLength="130" lengthAdjust="spacingAndGlyphs">CLIENT</text>
      <text class="value-title-shadow" x="658" y="834" textLength="167" lengthAdjust="spacingAndGlyphs">FOCUSED</text>
      <text class="value-title" x="655" y="831" textLength="167" lengthAdjust="spacingAndGlyphs">FOCUSED</text>
      <text class="value-copy">
        <tspan x="652" y="906">We provide a personal</tspan>
        <tspan x="652" y="927">service that goes above</tspan>
        <tspan x="652" y="949">the standards of</tspan>
        <tspan x="652" y="970">professional care.</tspan>
      </text>

      <text class="value-title-shadow" x="302" y="1108" textLength="201" lengthAdjust="spacingAndGlyphs">RECTITUDE</text>
      <text class="value-title" x="299" y="1105" textLength="201" lengthAdjust="spacingAndGlyphs">RECTITUDE</text>
      <text class="value-copy">
        <tspan x="318" y="1133">We know the</tspan>
        <tspan x="318" y="1154">difference between</tspan>
        <tspan x="318" y="1176">what we have the right</tspan>
        <tspan x="318" y="1198">to do and what the</tspan>
        <tspan x="318" y="1219">right thing to do is.</tspan>
      </text>

      <text class="value-title-shadow" x="644" y="1101" textLength="192" lengthAdjust="spacingAndGlyphs">EMPOWER</text>
      <text class="value-title" x="641" y="1098" textLength="192" lengthAdjust="spacingAndGlyphs">EMPOWER</text>
      <text class="value-copy">
        <tspan x="694" y="1142">We are dedicated,</tspan>
        <tspan x="694" y="1163">appreciative and</tspan>
        <tspan x="694" y="1185">respectful of</tspan>
        <tspan x="694" y="1206">people’s time</tspan>
        <tspan x="694" y="1228">and purpose.</tspan>
      </text>
    </g>

    <g class="brand-promise">
      <path class="promise-cap" d="M248,1405 L248,1400 C248,1360 285,1327 340,1327 L800,1327 C855,1327 892,1360 892,1400 L892,1405 Z" fill="var(--trunk)"/>
      <text class="promise-title" x="570" y="1388" text-anchor="middle">BRAND PROMISE</text>
      <rect class="promise-band" x="248" y="1405" width="644" height="113" fill="var(--sky-teal)"/>
      <line x1="382" y1="1415" x2="382" y2="1505" stroke="var(--icon-line)" stroke-width="2"/>
      <line x1="632" y1="1415" x2="632" y2="1505" stroke="var(--icon-line)" stroke-width="2"/>

      <g class="promise-icon icon-trust">
        <path d="M298,1440 L312,1426 L326,1434 L338,1424"/>
        <path d="M300,1442 L318,1458 L336,1444"/>
        <circle cx="333" cy="1419" r="7"/>
      </g>
      <g class="promise-icon icon-transparency">
        <circle cx="496" cy="1428" r="15"/>
        <ellipse cx="496" cy="1428" rx="9" ry="5"/>
        <line x1="507" y1="1439" x2="520" y2="1455"/>
      </g>
      <g class="promise-icon icon-dependability">
        <rect x="733" y="1432" width="8" height="20"/>
        <path d="M743,1434 L750,1424 L752,1416 C757,1416 758,1422 756,1430 L770,1430 L770,1452 L743,1452 Z"/>
        <line x1="744" y1="1412" x2="742" y2="1406"/>
        <line x1="754" y1="1410" x2="754" y2="1403"/>
        <line x1="764" y1="1412" x2="766" y2="1406"/>
      </g>

      <text class="promise-label" x="274" y="1505" textLength="86" lengthAdjust="spacingAndGlyphs">TRUST</text>
      <text class="promise-label" x="399" y="1505" textLength="219" lengthAdjust="spacingAndGlyphs">TRANSPARENCY</text>
      <text class="promise-label" x="647" y="1505" textLength="212" lengthAdjust="spacingAndGlyphs">DEPENDABILITY</text>
    </g>
  </g>
</svg>
</body>
</html>
```